Flyer-Design für nachhaltige Familienberatung
Reiche Ideenvielfalt (viele sehr verschiedene Designvorschläge), prompte Umsetzung aller Änderungsideen während und nach dem Wettbewerb und dazu ein sehr freundlicher Kontakt - so macht die Zusammenarbeit wirklich Spaß! Vielen Dank dafür!
Zielgruppe
Ich bin Kleinunternehmerin und berate junge Familien (auch Schwangere, Alleinerziehende und andere Angehörige) zu den Themen Stoffwindeln, Windelfrei, Babyschlaf und bedürfnis-/bindungsorientierter Erziehung. Außerdem biete ich Paarberatung und Einzelcoaching für Mütter und - gemeinsam mit meinem Mann - für Väter an.
Der Name 'Familie LuTi' steht für Lotte und Timo, mich und meinem Mann, gleichzeitig ein Wortspiel mit einer 'Hasenfamilie', auf das gern angespielt werden kann.
Weitere Informationen zum Angebot können der Internetseite www.familie-luti.de entnommen werden.
Aufgabenstellung
Das Design sollte farblich und stilistisch zum Logo passen. Naturverbundenheit/Nachhaltigkeit und Familienleben/Geborgenheit dürfen im Mittelpunkt stehen.
Mein Angebot ist vielfältig - umso wichtiger ist eine übersichtliche klare Darstellung. Der Flyer sollte junge Familien ansprechen. Er sollte hochwertig und liebevoll wirken: die Leser*innen sollten ermutigt werden, mich einfach unverbindlich anzurufen/mir zu schreiben (E-Mail, Pingora, ChatBrix, Freundbuch-Messenger) und mehr über das Angebot zu erfahren.
Die Flyer werden vor allem in Geburtshäusern, Krankenhäusern, Familienzentren und bei Frauen-/Kinderärzt*innen und Hebammen ausliegen. Außerdem werden sie durch Kooperationspartner*innen (Still-/Trageberaterinnen, in Geburtsvorbereitungskursen) verteilt.
Die hochgeladenen Fotos dürfen, müssen aber nicht verwendet werden.

```html
<!DOCTYPE html>
<html lang="de">
<head>
<meta charset="utf-8">
<title>Familie LuTi – Flyer</title>
<link href="https://fonts.googleapis.com/css2?family=Cinzel:wght@400;500&family=Jost:wght@400&display=swap" rel="stylesheet">
<style>
:root{
  --backdrop:#ece8e1;
  --green:#9cbf78;
  --green-mid:#93b76f;
  --orange:#e07a2a;
  --white:#ffffff;
  --photo-warm:#8a6a4a;
  --photo-leaf:#6f8a4a;
}
*{box-sizing:border-box;margin:0;padding:0}
html,body{width:1200px;height:3419px;overflow:hidden;background:var(--backdrop)}
body{position:relative;font-family:"Jost",sans-serif;color:var(--white)}
.spread{position:absolute;left:0;width:1200px;display:flex}
.spread--outside{top:878px;height:851px}
.spread--inside{top:2563px;height:856px}
.panel{position:relative;width:400px;height:100%;background:var(--green);overflow:hidden}
.panel--mid{background:var(--green-mid);border-left:1px solid rgba(0,0,0,.08);border-right:1px solid rgba(0,0,0,.08)}
.block{position:absolute;left:40px;width:320px}
.body-text{font-size:13.6px;line-height:1.28;hyphens:auto}
.body-text p+p{margin-top:14px}
.heading{font-family:"Cinzel",serif;color:var(--orange);font-size:15px;line-height:1.1;letter-spacing:.04em;text-transform:uppercase}
.heading--right{text-align:right}
.photo{position:absolute;left:0;width:100%}
.photo--bottom{bottom:0}
.photo--top{top:0}
.fade-up{-webkit-mask-image:linear-gradient(to bottom,transparent,#000 35%);mask-image:linear-gradient(to bottom,transparent,#000 35%)}
.fade-down{-webkit-mask-image:linear-gradient(to top,transparent,#000 35%);mask-image:linear-gradient(to top,transparent,#000 35%)}
.quote{position:absolute;left:40px;width:320px;text-align:center;font-family:"Cinzel",serif;font-size:15px;line-height:1.15;letter-spacing:.03em}
.quote-source{position:absolute;left:40px;width:320px;text-align:center;font-family:"Cinzel",serif;font-size:11px;letter-spacing:.05em;line-height:1.25}
.brand-mark{position:absolute;left:0;width:100%;text-align:center}
.brand-mark .dot{display:block;margin:0 auto 10px;width:54px;height:54px;border-radius:50%;background:var(--orange)}
.brand-mark .name{font-family:"Cinzel",serif;color:var(--orange);font-size:14px;letter-spacing:.06em}
.contact{position:absolute;left:40px;width:320px;display:flex;justify-content:space-between;font-family:"Cinzel",serif;font-size:11px;letter-spacing:.05em;line-height:1.3}
.title{position:absolute;left:0;width:100%;text-align:center;font-family:"Cinzel",serif;color:var(--orange);font-size:39px;letter-spacing:.04em}
.tagline{position:absolute;left:0;width:100%;text-align:center;font-family:"Cinzel",serif;font-size:13.5px;letter-spacing:.06em}
.offer{position:absolute;left:86px}
.offer text{font-family:"Cinzel",serif;font-size:14px;fill:var(--white);letter-spacing:.12em}
</style>
</head>
<body>

<!-- Außenseite -->
<section class="spread spread--outside">
  <div class="panel">
    <h2 class="heading block" style="top:44px">Begleitung und Beratung</h2>
    <div class="block body-text" style="top:74px">
      <p>Stillen, wickeln, tragen, schlafen, wickeln, spielen, stillen, wickeln… Der Alltag als junge Familie ist plötzlich ganz anders als bisher. Andere Dinge sind wichtig geworden und die ein oder andere Situation kann ganz schön überfordern. Da kommt so ein kleines Wunder zur Welt und plötzlich ist man Eltern. Das kann ein Ungleichgewicht in die Beziehung bringen. Eine Paarberatung kann euch helfen, wieder miteinander ins Gespräch zu kommen und einen gemeinsamen Weg als Liebespaar und Eltern zu finden.</p>
      <p>Auch als einzelne (werdende) Elternteile könnt ihr gern eine Beratung in Anspruch nehmen. Zum Beispiel, wenn ihr das Gefühl habt, von eurer neuen Rolle oder all den gut gemeinten Ratschlägen aus dem Umfeld überfordert zu sein oder einfach gar nicht mehr wisst, wo euch der Kopf steht. Wenn ihr für euch selbst gut sorgt, habt ihr mehr Energie, das Familienleben zu meistern, ja sogar zu genießen.</p>
      <p>Zu wagen, den eigenen Weg (oder den der Eltern, Freund*innen, …) zu hinterfragen, kann spannende neue Perspektiven eröffnen. Sich zu lösen von starren Idealen und der einen Idee, wie „man“ es „richtig“ macht, die aber leider nicht zum eigenen Kind oder euch selbst passt, kann entlasten und regelrecht heilsam sein. Bedürfnisse wahrnehmen und respektieren, Bindungen stärken und natürlich leben, einander zu Wort kommen lassen (egal wie alt das Gegenüber ist), das sind unsere Herzensanliegen, bei denen wir euch gern unterstützen.</p>
    </div>
    <div class="photo photo--bottom fade-up" style="height:280px;background:linear-gradient(180deg,#7c9a5a,#4f6a38 60%,#6b5a3e)" role="img" aria-label="Foto: Paar im Park auf einer Holzbank, Wiese und Bäume im Gegenlicht"></div>
  </div>

  <div class="panel panel--mid">
    <div class="photo photo--top fade-down" style="height:380px;background:linear-gradient(180deg,#7a7a3e,#a8683e 55%,#b35a4a)" role="img" aria-label="Foto: lächelnde Frau mit Stirnband hält einen Stapel bunter Stoffwindeln"></div>
    <p class="quote" style="top:449px">»Zwei Dinge hatten wir, die unsere Kindheit zu dem machten, wie sie war – Geborgenheit und Freiheit.«</p>
    <p class="quote-source" style="top:568px">Ingrid Lundgren &amp; Marita Strandqvist<br>in »Mein Heideland«</p>
    <div class="brand-mark" style="top:660px"><span class="dot"></span><span class="name">FAMILIE LUTI</span></div>
    <div class="contact" style="top:786px">
      <span>Birkenallee 5<br>37199 Waldheim</span>
      <span>T. 0151 23 45 67 89<br>www.familie-luti.de</span>
    </div>
  </div>

  <div class="panel">
    <h1 class="title" style="top:40px">FAMILIE LUTI</h1>
    <p class="tagline" style="top:98px">BERATUNG—BEGLEITUNG—WORKSHOPS</p>

    <svg class="offer" style="top:118px" width="240" height="190" viewBox="0 0 240 190" aria-label="Babyschlafcoaching">
      <defs><path id="arc1" d="M32 92 A88 88 0 1 0 187 35"/></defs>
      <circle cx="120" cy="92" r="70" fill="var(--orange)"/>
      <circle cx="120" cy="92" r="62" fill="#4e5d7a" role="img" aria-label="Foto: schlafendes Baby mit Teddybär"/>
      <text><textPath href="#arc1" startOffset="4%">BABYSCHLAFCOACHING</textPath></text>
    </svg>
    <svg class="offer" style="top:290px" width="240" height="190" viewBox="0 0 240 190" aria-label="Windelfreiberatung">
      <defs><path id="arc2" d="M32 92 A88 88 0 1 0 187 35"/></defs>
      <circle cx="120" cy="92" r="70" fill="var(--orange)"/>
      <circle cx="120" cy="92" r="62" fill="#c9a88c" role="img" aria-label="Foto: Kleinkind auf einem Töpfchen mit bunten Bällen"/>
      <text><textPath href="#arc2" startOffset="4%">WINDELFREIBERATUNG</textPath></text>
    </svg>
    <svg class="offer" style="top:476px" width="240" height="190" viewBox="0 0 240 190" aria-label="Stoffwindelberatung">
      <defs><path id="arc3" d="M32 92 A88 88 0 1 0 187 35"/></defs>
      <circle cx="120" cy="92" r="70" fill="var(--orange)"/>
      <circle cx="120" cy="92" r="62" fill="#6f8a4a" role="img" aria-label="Foto: Baby in Stoffwindel krabbelt durchs Gras"/>
      <text><textPath href="#arc3" startOffset="2%">STOFFWINDELBERATUNG</textPath></text>
    </svg>
    <svg class="offer" style="top:635px" width="240" height="190" viewBox="0 0 240 190" aria-label="Paar- und Einzelcoaching">
      <defs><path id="arc4" d="M32 92 A88 88 0 1 0 187 35"/></defs>
      <circle cx="120" cy="92" r="70" fill="var(--orange)"/>
      <circle cx="120" cy="92" r="62" fill="#5e7446" role="img" aria-label="Foto: Paar auf einer Parkbank"/>
      <text style="font-size:13px;letter-spacing:.08em"><textPath href="#arc4" startOffset="0%">PAAR- UND EINZELCOACHING</textPath></text>
    </svg>
  </div>
</section>

<!-- Innenseite -->
<section class="spread spread--inside">
  <div class="panel">
    <h2 class="heading block" style="top:42px">Wir bieten euch Beratung<br>und Unterstützung…</h2>
    <div class="block body-text" style="top:95px">
      <p>Wir glauben, dass jeder Mensch sein Bestes geben möchte. Als Elternteil, als Kind, als Partner*in, als Mensch. Aber das ist oft gar nicht so einfach. Freundlich zu bleiben, wenn man schon zu spät dran ist – gelassen zu bleiben, wenn das Baby schon wieder nicht einschlafen kann (oder etwa nicht will?!) – ein bisschen Umwelt retten, wenn die To-Do-Liste doch noch so lang ist – wie soll das nur gehen? Wir möchten euch dabei unterstützen, euren eigenen Weg zu finden und euch dabei nicht selbst zu verlieren.</p>
      <p>Dabei ist es uns wichtig, euch nicht nur ein Bausteinchen anzubieten, sondern nach und nach ein ganzes Mosaik. Denn viele Themen, die euch beschäftigen, hängen eng miteinander zusammen. Wobei wir euch tatsächlich begleiten dürfen, entscheidet selbstverständlich ihr.</p>
    </div>
    <h3 class="heading heading--right block" style="top:447px">…bei unruhigen Nächten<br>mit eurem Baby</h3>
    <div class="block body-text" style="top:500px">
      <p>Mit der Geburt eines Kindes ist es aus mit den ruhigen Nächten, hört man oft. Doch lange Nächte zehren an den Kräften der Eltern und nicht selten fühlen sie sich allein gelassen. Mit einer bindungs-</p>
    </div>
    <div class="photo photo--bottom fade-up" style="height:260px;background:linear-gradient(180deg,#7f8aa0,#8a6a4a 55%,#3e4d6a)" role="img" aria-label="Foto: schlafendes Baby im Sternenschlafanzug mit Teddybär"></div>
  </div>

  <div class="panel panel--mid">
    <div class="photo photo--top fade-down" style="height:310px;background:linear-gradient(180deg,#6a5448,#d8d2cc 45%,#c8c0a8)" role="img" aria-label="Foto: Kleinkind auf einem weißen Töpfchen, bunte Bälle und Stapelbecher"></div>
    <div class="block body-text" style="top:352px">
      <p>orientierten Schlafberatung kann ein artgerechter Weg zu besserem und erholsamerem Schlaf für Eltern und Kind(er) von etwa 0-2 Jahren gefunden werden.</p>
      <p>Ein Grund, warum ein Baby unruhig schläft, kann sein, dass es mal muss. Dann hilft es, ihm die Chance auf eine trockene und ruhige Nacht zu geben:</p>
    </div>
    <h3 class="heading heading--right block" style="top:534px">…beim trocken bleiben<br>oder werden</h3>
    <div class="block body-text" style="top:584px">
      <p>Schon Neugeborene haben ein angeborenes Bedürfnis nach Sauberkeit, dem Eltern ohne viel Aufwand entgegen kommen können. Oder es vielleicht erstmal ausprobieren und dann weitersehen. In einer Windelfrei/Hello-Nappy-Beratung erfahrt ihr u.a., wie und wo Babys kindgerecht und entspannt ihr großes und kleines Geschäft machen können.</p>
      <p>Kinder, die mit dieser Methode aufgewachsen sind, sind oft schon mit weniger als einem Jahr trocken. Doch auch wenn euer Kind mit Windeln aufgewachsen ist und sich mit dem Trocken werden schwer tut, sind wir für euch da – und das ganz ohne zwanghaftes Toilettentraining.</p>
    </div>
  </div>

  <div class="panel">
    <div class="block body-text" style="top:42px">
      <p>Am Einfachsten lässt sich das umsetzen, wenn Stoffwindeln verwendet werden:</p>
    </div>
    <h3 class="heading heading--right block" style="top:132px">…beim Thema Stoffwindeln</h3>
    <div class="block body-text" style="top:160px">
      <p>Stoffwindeln sind gesünder, ökologischer und langfristig kostengünstiger als Wegwerfwindeln und dabei genauso leicht zu benutzen. Außerdem verlieren Babys und Kleinkinder, die mit Stoff gewickelt werden, nicht das Gefühl für ihre Ausscheidungen und werden so häufig (ohne hello nappy) bereits mit unter zwei Jahren trocken.</p>
      <p>Damit ihr aus dem scheinbar undurchdringlichen (Stoffwindel)Dschungel ins bunte Paradies findet, in dem es für jedes Kind und jede Betreuungsperson die passende, einfache, schöne Windel gibt, beraten wir euch gern. Ihr lernt die verschiedenen modernen Windelsysteme kennen, könnt die Materialien anfassen und die Anwendung an Stoffpuppen ausprobieren.</p>
    </div>
    <div class="photo photo--bottom fade-up" style="height:400px;background:linear-gradient(180deg,#8aa862,#5f7f3e 50%,#7a9a4e)" role="img" aria-label="Foto: Baby in bunter Stoffwindel krabbelt über eine Blumenwiese"></div>
  </div>
</section>

</body>
</html>
```